Need 8.5" x 11" as well as large 11"x17" Posters for our upcoming eventPlease include LOGOs in poster Main logo is Interfaith Youth Council of OCInfo/Content to include:All high school age faith groups are invited to come and join with 150 to 175 other high school students from various faith traditions to participate in the Harborlight Teen Circle of Willow Vale‘s Annual Harborlight Teen Gathering. More than ever, our county and the world needs young leaders who are willing to learn from each other and build stronger communities!FAITH FORUMThe purpose of this Harborlight Teen Gathering is to bring together young people from diverse ethnic, cultural, and religious backgrounds, and to engage them in dialogue. True dialogue is a conversation on a common subject between two or more persons of differing points of view and/or backgrounds. We feel that this commitment to dialogue will affect relationships in a constructive way in our places of worship and in our community.The forum itself involves having eight religiously diverse high school-age students, one adult, and youth leader around each table to discuss common questions. Our youth leaders act as facilitators, but it is stressed that it is the students we want to hear from.
Registration is Required for our KINDRED TABLE before February 25th, 2019
FORUM QUESTIONS and rregistration available online at http://htcwv-example.org/home/kindred-fair/

Target Market(s)

Houses of worship, community leaders, High School Students

Industry/Entity Type

Non-Profit

Font styles to use
Serif

Colors
fefcec
f78f20
faa54b
fece3e
3176b5
33a6d7
0592cd
0455a3
f68d4d

Requirements
Must have
• Must Have:
• - Harborlight Teen Circle of Willow Vale's 15th Annual Kindred Table & Fair
• - TEENS EXPRESSING THEIR FAITH THROUGH ART, MUSIC, AND DIALOGUE
• - THIS YEAR'S THEME: "Threads of Belief"
• - Sunday, March 10th, 2019 1:30pm-6:30pm
• - The Fellowship Hall of Saint Verran's Meadow Parish
• - 4738 Tamsworth Glen Road Willow Vale, CA 90000
• - Email: htcwvorg@mailbox-example.com
• - Website: HTCWV-example.org
• - Facebook: Harborlight Teen Circle of Willow Vale
• Please include pictures provided
• Logo must be on there and prominent: Harborlight Teen circle of Willow Vale
• second logo should be somewhere on the bottom or back: Brightmoor Allied Fund
Nice to have
• Descriptions provided in word doc
• Ideally would like Logo and pictures and main info on the front
• - Website: HTCWV-example.org
• On the back have more details about the program and pics if needed

```html
<!DOCTYPE html>
<html lang="en">
<head>
<meta charset="utf-8">
<title>Harborlight Teen Circle of Willow Vale – 15th Annual Kindred Table &amp; Fair</title>
<link rel="stylesheet" href="https://fonts.googleapis.com/css2?family=Arvo:ital,wght@0,400;0,700;1,700&family=Libre+Baskerville:ital,wght@0,400;0,700;1,400;1,700&family=Roboto:wght@400;500&display=swap">
<style>
:root{
  --backdrop:#b5b4b5;
  --paper:#ffffff;
  --orange:#f78f20;
  --orange-light:#faa54b;
  --blue:#0455a3;
  --blue-mid:#3176b5;
  --ink:#333333;
  --ink-soft:#444444;
}
*{margin:0;padding:0;box-sizing:border-box}
html,body{width:1200px;height:1200px;overflow:hidden;background:var(--backdrop)}
.page{position:absolute;top:286px;width:489px;height:629px;background:var(--paper);overflow:hidden;font-family:"Libre Baskerville",serif;color:var(--ink)}
.page--front{left:74px}
.page--back{left:638px}
.abs{position:absolute}
.photo{position:absolute}

/* front */
.org-title{left:0;width:489px;top:12px;text-align:center;font-weight:700;font-size:20.5px;white-space:nowrap;color:var(--ink)}
.brand-mark{left:22px;top:46px;width:102px;height:102px;border:2px solid #222;border-radius:50%;display:flex;align-items:center;justify-content:center;text-align:center;font-weight:700;font-size:9.5px;line-height:1.3;color:#222;padding:10px}
.event-number{left:153px;top:42px;font-family:"Arvo",serif;font-weight:700;font-size:35px;color:var(--orange);line-height:1}
.event-name{left:150px;top:84px;font-family:"Arvo",serif;font-weight:700;font-size:30px;color:var(--blue);line-height:1;white-space:nowrap}
.event-host{left:152px;top:119px;font-weight:700;font-size:14.8px;color:var(--ink);white-space:nowrap}
.theme-tab{left:0;top:156px;width:179px;height:38px;background:var(--orange);color:#fff;text-align:center}
.theme-tab .label{display:block;font-size:7.5px;margin-top:5px;letter-spacing:.2px}
.theme-tab .theme{display:block;font-weight:700;font-size:12.5px;margin-top:3px;white-space:nowrap}
.date-band{left:179px;top:166px;width:310px;height:38px;background:var(--orange-light);color:#fff;font-weight:700;font-size:12.4px;display:flex;align-items:center;padding-left:9px;white-space:nowrap}
.partner-mark{left:20px;top:378px;width:100px;display:flex;align-items:center;gap:6px}
.partner-mark .dot{width:14px;height:14px;border-radius:50%;background:var(--blue-mid);flex:none}
.partner-mark .name{font-size:11px;line-height:1.15;color:var(--blue-mid)}
.tagline{left:129px;top:371px;font-weight:700;font-size:7.6px;white-space:nowrap}
.venue{left:129px;top:387px;font-weight:700;font-size:10.6px;white-space:nowrap}
.address{left:129px;top:405px;font-family:"Arvo",serif;font-weight:700;font-size:11.8px;color:var(--orange);white-space:nowrap}
.intro{left:19px;top:432px;width:455px;font-family:"Roboto",sans-serif;font-size:6.6px;line-height:1.28;color:var(--ink-soft)}
.section-head{left:19px;top:467px;font-family:"Arvo",serif;font-weight:700;font-size:13.5px;color:var(--blue)}
.col{font-family:"Roboto",sans-serif;font-size:6.6px;line-height:1.28;color:var(--ink-soft);text-align:justify}
.col--left{left:19px;top:489px;width:166px}
.col--right{left:212px;top:488px;width:259px}
.rsvp{left:206px;top:530px;width:271px;text-align:center;font-weight:700;font-size:11.8px;line-height:1.3;white-space:nowrap}
.rsvp .when{color:var(--blue);font-family:"Arvo",serif;font-size:13px}
.online{left:20px;top:570px;white-space:nowrap;font-weight:700;font-size:8px}
.online .url{font-family:"Arvo",serif;font-size:11px;color:var(--orange)}
.footer{left:0;top:597px;width:489px;height:32px;background:var(--blue);color:#fff;font-family:"Roboto",sans-serif;font-size:8px;display:flex;align-items:center;justify-content:space-between;padding:0 18px}
.footer span{display:flex;align-items:center;gap:4px;white-space:nowrap}
.footer svg{flex:none}

/* back */
.q-title{left:20px;top:14px;font-family:"Arvo",serif;font-weight:700;font-size:20.5px;color:var(--blue);white-space:nowrap}
.q-theme{left:13px;top:43px;width:143px;height:24px;border:1px solid #555;color:var(--orange);font-size:12px;display:flex;align-items:center;justify-content:center;white-space:nowrap}
.icebreaker{left:20px;top:75px;font-weight:700;font-style:italic;font-size:11.5px;color:var(--blue)}
.ice-q{left:20px;top:94px;font-weight:700;font-size:7.5px}
.q-head{left:20px;font-style:italic;font-size:8.5px;color:var(--orange);white-space:nowrap}
.q-list{left:20px;width:250px;font-family:"Roboto",sans-serif;font-size:6px;line-height:1.3;color:var(--ink-soft);list-style:none}
.q-list li{display:flex;margin-bottom:6px}
.q-list li b{font-weight:400;width:14px;flex:none}
.q-list li.sub{padding-left:28px}
.q-list--wide{width:330px}
.q-list--wide li{margin-bottom:4.2px}
.reflection{left:30px;top:564px;width:429px;text-align:center;font-family:"Roboto",sans-serif;font-size:8.6px;line-height:1.35;color:#222}
</style>
</head>
<body>

<section class="page page--front">
  <h1 class="abs org-title">Harborlight Teen Circle of Willow Vale's</h1>
  <div class="abs brand-mark">Harborlight Teen Circle of Willow Vale</div>
  <div class="abs event-number">15th Annual</div>
  <div class="abs event-name">Kindred Table &amp; Fair</div>
  <div class="abs event-host">Harborlight Teen Circle of Willow Vale</div>

  <div class="abs theme-tab"><span class="label">THIS YEAR'S THEME</span><span class="theme">"Threads of Belief"</span></div>
  <div class="abs date-band">Sunday, March 10th, 2019 1:30pm-6:30pm</div>

  <div class="photo" role="img" aria-label="Four smiling teen volunteers in matching brown shirts outdoors" style="left:3px;top:198px;width:162px;height:156px;background:linear-gradient(160deg,#d9cfc2,#7a5a44 60%,#5b4030)"></div>
  <div class="photo" role="img" aria-label="Crowded hall of students seated at round tables" style="left:168px;top:206px;width:154px;height:69px;background:linear-gradient(180deg,#8d8a86,#5e5350)"></div>
  <div class="photo" role="img" aria-label="Row of youth leaders standing on stage behind a table" style="left:325px;top:206px;width:164px;height:82px;background:linear-gradient(180deg,#b8b0a6,#6c5444 70%,#e8e6e4)"></div>
  <div class="photo" role="img" aria-label="Students in discussion around a table with papers" style="left:171px;top:278px;width:151px;height:77px;background:linear-gradient(180deg,#6f6564,#b6a7b8)"></div>
  <div class="photo" role="img" aria-label="Colourful banners of faith traditions on a maroon table" style="left:325px;top:290px;width:164px;height:64px;background:linear-gradient(90deg,#6a1f2a,#c44a3c 45%,#6e84c4 70%,#5a1a26)"></div>

  <div class="abs partner-mark"><span class="dot"></span><span class="name">Brightmoor Allied Fund</span></div>
  <div class="abs tagline">TEENS EXPRESSING THEIR FAITH THROUGH ART, MUSIC, AND DIALOGUE</div>
  <div class="abs venue">The Fellowship Hall of Saint Verran's Meadow Parish</div>
  <div class="abs address">4738 Tamsworth Glen Road Willow Vale, CA 90000</div>

  <p class="abs intro">All high school age faith groups are invited to come and join with 150 to 175 other high school students from various faith traditions to participate in the Harborlight Teen Circle of Willow Vale's Annual Harborlight Teen Gathering. More than ever, our county and the world needs young leaders who are willing to learn from each other and build stronger communities!</p>

  <h2 class="abs section-head">KINDRED TABLE</h2>
  <p class="abs col col--left">The purpose of this Harborlight Teen Gathering is to bring together young people from diverse ethnic, cultural, and religious backgrounds, and to engage them in dialogue. True dialogue is a conversation on a common subject between two or more persons of differing points of view and/or backgrounds. We feel that this commitment to dialogue will affect relationships in a constructive way in our places of worship and in our community.</p>
  <p class="abs col col--right">The forum itself involves having eight religiously diverse high school-age students, one adult, and youth leader around each table to discuss common questions. Our youth leaders act as facilitators, but it is stressed that it is the students we want to hear from.</p>
  <div class="abs rsvp">RSVP for our KINDRED TABLE before<br><span class="when">February 25th, 2019</span></div>
  <div class="abs online">FORUM QUESTIONS Available online at <span class="url">http://htcwv-example.org/home/kindred-fair/</span></div>

  <footer class="abs footer">
    <span><svg width="9" height="7" viewBox="0 0 9 7"><rect x=".5" y=".5" width="8" height="6" fill="none" stroke="#fff"/><path d="M.5 .5 4.5 4 8.5 .5" fill="none" stroke="#fff"/></svg>htcwvorg@mailbox-example.com</span>
    <span><svg width="8" height="8" viewBox="0 0 8 8"><circle cx="4" cy="4" r="3.4" fill="none" stroke="#fff"/><path d="M.6 4h6.8M4 .6c-2 2-2 4.8 0 6.8M4 .6c2 2 2 4.8 0 6.8" fill="none" stroke="#fff" stroke-width=".7"/></svg>HTCWV-example.org</span>
    <span><svg width="7" height="7" viewBox="0 0 7 7"><circle cx="3.5" cy="3.5" r="3" fill="#fff"/></svg>Harborlight Teen Circle of Willow Vale</span>
  </footer>
</section>

<section class="page page--back">
  <h2 class="abs q-title">2019 Forum Questions</h2>
  <div class="abs q-theme">"Threads of Belief"</div>
  <div class="photo" role="img" aria-label="Smiling dancer in a red and yellow costume with arms raised" style="left:275px;top:0;width:214px;height:332px;background:linear-gradient(180deg,#e7e3de,#c9a25a 35%,#c8302c 75%,#9e1f1f)"></div>

  <div class="abs icebreaker">ICE BREAKER QUESTION:</div>
  <div class="abs ice-q">What is your favorite aspect of your faith?</div>

  <div class="abs q-head" style="top:111px">1)&nbsp; How has your culture influenced your faith?</div>
  <ol class="abs q-list" style="top:128px">
    <li><b>a)</b>How do people of your faith practice it differently in other parts of the world?</li>
    <li><b>b)</b>In what ways have others' opinions of your faith changed and what has led to those changes?</li>
    <li><b>c)</b>In what ways does your culture directly alter the practice of your faith? Give an example from your culture and your scripture.</li>
  </ol>

  <div class="abs q-head" style="top:197px">2)&nbsp; How has your faith changed since past generations?</div>
  <ol class="abs q-list" style="top:216px">
    <li><b>a)</b>How do you practice your faith differently than your parents or grand-parents?</li>
    <li class="sub">i) How are the societal problems that you face different from what past generations have faced?</li>
    <li><b>b)</b>Do you believe that your faith practices will change in the future? If so, in what ways?</li>
    <li><b>c)</b>In your faith's scripture(s) and history, does discrimination and acts of persecution come up? If so, what is the solution given from your teachings?</li>
    <li><b>d)</b>Have you ever suffered discrimination or acts of violence? In what ways did you overcome it using your teachings?</li>
  </ol>

  <div class="abs q-head" style="top:339px">3)&nbsp; How have some current events affected you?</div>
  <ol class="abs q-list q-list--wide" style="top:357px">
    <li><b>a)</b>What does your tradition say about immigration, homelessness, #metoo movement, refugees, etc.?</li>
    <li><b>b)</b>What does your faith say about treating "the other"? (Use history, scripture etc.)</li>
    <li><b>c)</b>How has your religion influenced your moral obligations? E.g. homelessness, refugees, etc.</li>
    <li><b>d)</b>In what ways could your faith community take action?</li>
  </ol>

  <svg class="abs" style="left:0;top:335px" width="489" height="218" viewBox="0 335 489 218">
    <polygon role="img" aria-label="Teen musicians playing string instruments on stage" points="0,417 166,417 142,553 0,553" fill="#8a6e62"/>
    <polygon role="img" aria-label="Art supplies and paper signs on a craft table" points="168,417 342,417 316,553 144,553" fill="#7f9a94"/>
    <polygon role="img" aria-label="Young drummer in a brown shirt playing large drums" points="360,335 489,335 489,553 318,553" fill="#8c4a2c"/>
  </svg>

  <p class="abs reflection">Reflection (closing): How, if any, has your experience at the youth forum changed how you&nbsp; relate to individuals of different faiths moving forward?</p>

  <footer class="abs footer">
    <span><svg width="9" height="7" viewBox="0 0 9 7"><rect x=".5" y=".5" width="8" height="6" fill="none" stroke="#fff"/><path d="M.5 .5 4.5 4 8.5 .5" fill="none" stroke="#fff"/></svg>htcwvorg@mailbox-example.com</span>
    <span><svg width="8" height="8" viewBox="0 0 8 8"><circle cx="4" cy="4" r="3.4" fill="none" stroke="#fff"/><path d="M.6 4h6.8M4 .6c-2 2-2 4.8 0 6.8M4 .6c2 2 2 4.8 0 6.8" fill="none" stroke="#fff" stroke-width=".7"/></svg>HTCWV-example.org</span>
    <span><svg width="7" height="7" viewBox="0 0 7 7"><circle cx="3.5" cy="3.5" r="3" fill="#fff"/></svg>Harborlight Teen Circle of Willow Vale</span>
  </footer>
</section>

</body>
</html>
```